My business is Property developing Stationary

I want business card and stationery. Please have the formate so I can edit details on card and stationary.

Please see my logo and on the back of the card I want it same red as my logo and I will provide copy that I want on the back of the card.

Also need an email signature

On the business card and email signature add below copy:
Project Management- Acquisitions- Syndicates- Joint Ventures

Target Market(s)

Property investors

Industry/Entity Type

Business

Requirements
Must have
• Reflect my Logo

```html
<!DOCTYPE html>
<html lang="en">
<head>
<meta charset="utf-8">
<title>Corvela Property Developments — Stationery</title>
<link href="https://fonts.googleapis.com/css2?family=Montserrat:wght@500;700;800&family=Questrial&display=swap" rel="stylesheet">
<style>
  :root {
    --brand-red: #d63a2b;
    --band-black: #1b1b1b;
    --paper: #f7f7f7;
    --ink: #2a2a2a;
    --ink-soft: #5a5a5a;
    --backdrop: #d4d4d4;
  }
  * { margin: 0; padding: 0; box-sizing: border-box; }
  html, body { width: 1200px; height: 900px; overflow: hidden; }
  body {
    background: var(--backdrop);
    font-family: "Questrial", "Helvetica Neue", sans-serif;
    color: var(--ink);
    position: relative;
  }
  .sheet {
    position: absolute;
    background: var(--paper);
    box-shadow: 0 2px 6px rgba(0,0,0,.18);
    overflow: hidden;
  }

  /* brand name block */
  .brand-name {
    font-family: "Montserrat", sans-serif;
    font-weight: 800;
    color: var(--brand-red);
    letter-spacing: .02em;
    line-height: 1;
    display: block;
  }
  .brand-tagline {
    font-family: "Montserrat", sans-serif;
    font-weight: 700;
    color: var(--ink);
    line-height: 1.2;
    display: block;
  }

  /* footer band */
  .band {
    position: absolute; left: 0; right: 0; bottom: 0;
    display: flex;
  }
  .band .band-red { background: var(--brand-red); }
  .band .band-black { background: var(--band-black); flex: 1; }

  /* contact list */
  .contact-list { list-style: none; }
  .contact-list li { display: flex; align-items: center; }
  .contact-icon { flex: none; }

  /* ---------- Letterhead ---------- */
  .letterhead { left: 220px; top: 54px; width: 381px; height: 540px; }
  .letterhead .brand { position: absolute; left: 36px; top: 44px; }
  .letterhead .brand-name { font-size: 22px; }
  .letterhead .brand-tagline { font-size: 7.2px; margin-left: 10px; }
  .letterhead .contact-block { position: absolute; left: 286px; top: 44px; font-size: 5.4px; color: var(--ink); }
  .letterhead .contact-list li { gap: 3px; height: 7px; }
  .letterhead .contact-icon { width: 5px; height: 5px; }
  .letterhead .address { margin-top: 5px; line-height: 1.35; }
  .recipient { position: absolute; left: 36px; top: 120px; font-size: 6px; line-height: 1.3; color: var(--ink-soft); }
  .letter-body { position: absolute; left: 36px; top: 180px; width: 310px; font-size: 5.4px; line-height: 1.42; color: var(--ink-soft); text-align: justify; }
  .letter-body .salutation { color: var(--ink); font-weight: bold; margin-bottom: 7px; }
  .letter-body p { margin-bottom: 6px; }
  .sign-off { position: absolute; left: 36px; top: 346px; font-size: 5.6px; line-height: 1.4; color: var(--ink-soft); }
  .sign-off strong { color: var(--ink); }
  .signature-area { position: absolute; left: 88px; top: 334px; width: 84px; height: 40px; background: linear-gradient(90deg, rgba(70,90,190,.08), rgba(70,90,190,.14)); border-radius: 4px; }
  .letterhead .band { height: 8px; }
  .letterhead .band-red { width: 250px; }

  /* ---------- Presentation folder ---------- */
  .folder { left: 650px; top: 40px; width: 415px; height: 554px; background: var(--brand-red); border-radius: 3px; }
  .folder .spine { position: absolute; left: 26px; top: 0; bottom: 0; width: 1px; background: rgba(0,0,0,.12); }
  .folder .brand { position: absolute; left: 0; right: 0; top: 86px; text-align: center; }
  .folder .brand-name { color: #fff; font-size: 33px; }
  .folder .brand-tagline { color: #fde6e2; font-family: "Questrial", sans-serif; font-weight: 400; font-size: 11.5px; margin-top: 2px; }

  /* ---------- Business card front ---------- */
  .card-front { left: 79px; top: 637px; width: 163px; height: 90px; }
  .card-front .person { position: absolute; left: 11px; top: 21px; }
  .card-front .person-name { font-family: "Montserrat", sans-serif; font-weight: 700; font-size: 5.4px; color: var(--brand-red); display: block; }
  .card-front .person-role { font-size: 4.2px; color: var(--ink-soft); }
  .card-front .brand { position: absolute; right: 12px; top: 18px; text-align: right; }
  .card-front .brand-name { font-size: 13px; }
  .card-front .brand-tagline { font-size: 4.2px; }
  .card-front .contact-block { position: absolute; left: 11px; top: 66px; font-size: 3.8px; }
  .card-front .contact-list li { gap: 2px; height: 5px; }
  .card-front .contact-icon { width: 3.6px; height: 3.6px; }
  .card-front .address { position: absolute; right: 12px; top: 71px; font-size: 3.8px; text-align: right; line-height: 1.3; }
  .card-front .band { height: 4px; }
  .card-front .band-red { width: 86px; }

  /* ---------- Business card back ---------- */
  .card-back { left: 79px; top: 748px; width: 163px; height: 91px; background: var(--brand-red); }
  .card-back .brand { position: absolute; left: 0; right: 0; top: 35px; text-align: center; }
  .card-back .brand-name { color: #fff; font-size: 14px; }
  .card-back .brand-tagline { color: #fde6e2; font-size: 4.4px; font-weight: 500; }

  /* ---------- Envelope front ---------- */
  .envelope-front { left: 278px; top: 640px; width: 400px; height: 199px; }
  .envelope-front .brand { position: absolute; left: 22px; top: 28px; }
  .envelope-front .brand-name { font-size: 20px; }
  .envelope-front .brand-tagline { font-size: 6.6px; margin-left: 10px; }
  .envelope-front .address { position: absolute; left: 45px; top: 62px; font-size: 5px; line-height: 1.35; color: var(--ink-soft); }
  .envelope-front .band { height: 8px; }
  .envelope-front .band-red { width: 240px; }

  /* ---------- Envelope back ---------- */
  .envelope-back { left: 724px; top: 640px; width: 399px; height: 199px; }
  .envelope-back .flap { position: absolute; left: 0; top: 0; width: 399px; height: 56px; display: block; }
</style>
</head>
<body>

  <!-- Letterhead -->
  <section class="sheet letterhead" aria-label="Letterhead">
    <div class="brand">
      <span class="brand-name">CORVELA</span>
      <span class="brand-tagline">Property Developments</span>
    </div>

    <div class="contact-block">
      <ul class="contact-list">
        <li><svg class="contact-icon" viewBox="0 0 10 10"><rect width="10" height="10" rx="1.5" fill="#d63a2b"/><path d="M3 2.5l1.2 1.5-.7.8a4 4 0 0 0 1.7 1.7l.8-.7L7.5 7 6.8 8C4.5 7.7 2.3 5.5 2 3.2z" fill="#fff"/></svg>1300 482 716</li>
        <li><svg class="contact-icon" viewBox="0 0 10 10"><rect width="10" height="10" rx="1.5" fill="#d63a2b"/><rect x="2" y="3" width="6" height="4" fill="none" stroke="#fff" stroke-width=".8"/><path d="M2 3l3 2.3L8 3" fill="none" stroke="#fff" stroke-width=".8"/></svg>info@corvela.com</li>
        <li><svg class="contact-icon" viewBox="0 0 10 10"><rect width="10" height="10" rx="1.5" fill="#d63a2b"/><circle cx="5" cy="5" r="2.8" fill="none" stroke="#fff" stroke-width=".8"/><path d="M2.2 5h5.6M5 2.2v5.6" stroke="#fff" stroke-width=".6"/></svg>www.corvela.com</li>
      </ul>
      <p class="address">Level 12, Harbour Point<br>18 Kent Lane, Sydney</p>
    </div>

    <address class="recipient">
      Recipient's name<br>Lindenweg 7<br>20144 Hamburg<br>Germany
    </address>

    <div class="letter-body">
      <p class="salutation">Dear sir,</p>
      <p>Thank you for your interest in our upcoming residential projects. This letter sets out a short summary of the opportunities currently open to private investors and the next steps we propose.</p>
      <p>Our team manages each development from site acquisition through planning, construction and final settlement. Investors may join through a syndicate or a joint venture, with regular reports on progress, budget and returns at every stage.</p>
      <p>We would welcome the chance to meet and walk you through the current offering in more detail. Please contact our office to arrange a time that suits you.</p>
      <p>We look forward to hearing from you and to working together on your next property investment.</p>
    </div>

    <p class="sign-off">Yours Sincerely,<br><strong>Tessa Marlow</strong></p>
    <div class="signature-area" role="img" aria-label="Handwritten signature of Tessa Marlow"></div>

    <div class="band"><span class="band-red"></span><span class="band-black"></span></div>
  </section>

  <!-- Presentation folder -->
  <section class="sheet folder" aria-label="Presentation folder">
    <span class="spine"></span>
    <div class="brand">
      <span class="brand-name">CORVELA</span>
      <span class="brand-tagline">Property Developments</span>
    </div>
  </section>

  <!-- Business card front -->
  <section class="sheet card-front" aria-label="Business card front">
    <div class="person">
      <span class="person-name">LEON HARTLEY</span>
      <span class="person-role">Managing Director</span>
    </div>
    <div class="brand">
      <span class="brand-name">CORVELA</span>
      <span class="brand-tagline">Property Developments</span>
    </div>
    <div class="contact-block">
      <ul class="contact-list">
        <li><svg class="contact-icon" viewBox="0 0 10 10"><rect width="10" height="10" rx="1.5" fill="#d63a2b"/></svg>1300 482 716</li>
        <li><svg class="contact-icon" viewBox="0 0 10 10"><rect width="10" height="10" rx="1.5" fill="#d63a2b"/></svg>info@corvela.com</li>
        <li><svg class="contact-icon" viewBox="0 0 10 10"><rect width="10" height="10" rx="1.5" fill="#d63a2b"/></svg>www.corvela.com</li>
      </ul>
    </div>
    <p class="address">Level 12, Harbour Point<br>18 Kent Lane, Sydney</p>
    <div class="band"><span class="band-red"></span><span class="band-black"></span></div>
  </section>

  <!-- Business card back -->
  <section class="sheet card-back" aria-label="Business card back">
    <div class="brand">
      <span class="brand-name">CORVELA</span>
      <span class="brand-tagline">Property Developments</span>
    </div>
  </section>

  <!-- Envelope front -->
  <section class="sheet envelope-front" aria-label="Envelope front">
    <div class="brand">
      <span class="brand-name">CORVELA</span>
      <span class="brand-tagline">Property Developments</span>
    </div>
    <p class="address">Level 12, Harbour Point<br>18 Kent Lane, Sydney</p>
    <div class="band"><span class="band-red"></span><span class="band-black"></span></div>
  </section>

  <!-- Envelope back -->
  <section class="sheet envelope-back" aria-label="Envelope back">
    <svg class="flap" viewBox="0 0 399 56" aria-hidden="true">
      <polygon points="0,0 399,0 384,56 15,56" fill="#d63a2b"/>
    </svg>
  </section>

</body>
</html>
```